Flyer design

I am looking for a design for a double sided flyer. Details of each side as follows.

SIDE 1
Using the 'Brisk Home Loans' logo, also insert 'is your mortgage in good shape?' directly under the logo, (see business cards)

The flyer is to have the following also included:

'Get your Mortgage in shape for Summer'

'Refinance today and potentially receive upwards of $1,500*'

'100% free service'

'Mobile broker to your door, at your convenience'

Call Now 0400 372 948

Email 'dale@briskhomeloans.com.au'

Web www.briskhomeloans.com.au

(in smaller writing the following can be written) Re-finance before 2015 and not only will your Mortgage specialist find you a better product, but they will also rebate you 50% of their brokering commission. An average $500,000 loan is likely to result in over $1,500 cash back. Has there ever been a better reason to refinance?

5% of profits donated to our partner open harvest

SIDE 2
Using the 'Keel Realty Advisory' logo, also insert 'Cutting out the Fatty Commissions' directly under the logo, (see business cards)

'What are you doing with your equity?' (strong emphasis on this statement)

Speak to our investment specialist today and find out how you could potentially use your equity to build a positively geared investment portfolio without spending your own money.

'Your actions today will determine how you live tomorrow'.

Free 1 hour consultation
No selling, just transparent guidance on the in's and out's of property investing along with current hot spots and an analysis of your investment property portfolio potential.

WARNING: beware of typical 'Free' investment seminars where you are ultimately guided down a path to overprized, commission packed, apartments or house and land packages (choked full of

Keel Realty Advisory will not sell you property, only provide transparent guidance so ultimately you can make an informed decision.

It is correct nothing is for free, however, unlike most property investment advisers the only payment/commission Keel Realty Advisory receives is that paid from the bank through brokering the loan on your investment property (should you choose to purchase a property and allow us to broker your loan)

Call today for further information of this amazing offer
Updates

Thanks for your designs so far, I am looking to emphasis the logo's please use them as the main feature, keep it simple, I may need to cut out some of the information so its not too crowded. As well as the logo the other things that need to stand out is the $1,500 rebate and the 'What are you doing with your equity?'. Both these statements and the logo should stand out as soon as someone see the flyer. Feel free to leave out some of the other info if you feel the flyer will look better, I can add to it if need be, but the presentation is vital. Simple is the key. Thanks again. Dale

Thanks for your designs, I am still considering my options, however, the last 2 posted designs are on the right path. Thanks

Target Market(s)

Middle age, middle income property owners. Generally families.

Industry/Entity Type

Investment

Requirements
Must have
• Please make the 2 logo's the most prominent feature of the flyer

```html
<!DOCTYPE html>
<html lang="en">
<head>
<meta charset="utf-8">
<title>Brisk Home Loans &amp; Keel Realty Advisory Flyer</title>
<link href="https://fonts.googleapis.com/css2?family=Lato:wght@400;700;900&display=swap" rel="stylesheet">
<style>
:root{
  --red:#ee2b2f;
  --navy:#153a63;
  --navy-text:#1b3a64;
  --sky:#4fb9dc;
  --white:#ffffff;
  --ink:#1d1d1d;
  --page:#f3f3f3;
  --photo-warm-a:#e9f2f6;
  --photo-warm-b:#c9b29a;
  --photo-cool-a:#f4f6f8;
  --photo-cool-b:#9eb2c8;
  --map-a:#eeeeea;
  --map-b:#dcdcd6;
}
*{box-sizing:border-box;margin:0;padding:0}
html,body{width:1200px;height:900px;overflow:hidden}
body{background:var(--page);font-family:'Lato',sans-serif;position:relative}
.flyer{position:absolute;top:137px;width:450px;height:643px;background:var(--white);box-shadow:0 4px 14px rgba(0,0,0,.18);overflow:hidden}
.flyer--front{left:78px}
.flyer--back{left:662px}

/* front */
.promo-band{background:var(--red);height:76px;text-align:center;padding-top:14px}
.promo-band__title{color:var(--white);font-weight:900;font-size:16.5px;letter-spacing:.2px}
.promo-band__sub{color:var(--ink);font-weight:700;font-size:12px;margin-top:9px}
.photo{display:block;width:100%}
.photo--couple{height:175px;margin-top:4px;background:linear-gradient(120deg,var(--photo-warm-a) 0%,var(--photo-warm-b) 45%,#e6d8c8 70%,var(--photo-warm-a) 100%)}
.front-info{background:var(--navy);height:215px;color:var(--white);text-align:center;padding-top:16px;position:relative}
.front-info__heading{font-weight:900;font-size:15px;letter-spacing:.2px}
.front-info__body{font-size:9.3px;line-height:1.45;padding:9px 28px 0;text-align:center}
.pill-row{display:flex;justify-content:space-between;margin-top:12px}
.pill{background:var(--red);color:var(--white);font-size:10.5px;line-height:1.35;font-weight:400;height:34px;width:198px;display:flex;align-items:center;text-transform:uppercase}
.pill--left{border-radius:0 8px 8px 0;padding-left:20px;text-align:left}
.pill--right{border-radius:8px 0 0 8px;justify-content:flex-end;padding-right:20px;text-align:right}
.front-info__free{font-weight:700;font-size:18px;margin-top:14px}
.call-line{display:flex;align-items:center;gap:8px;margin-top:8px}
.call-line::before,.call-line::after{content:"";flex:1;height:2px;background:var(--red)}
.call-line__text{font-weight:700;font-size:20px;white-space:nowrap}
.front-footer{position:relative;height:173px}
.brand{position:absolute;display:flex;flex-direction:column;align-items:center}
.brand--mortgages{left:20px;top:38px;width:180px}
.brand__row{display:flex;align-items:center;gap:8px}
.brand__mark{width:16px;height:16px}
.brand__name{font-weight:700;font-size:22px;color:var(--red);white-space:nowrap}
.brand__tag{font-size:8px;text-transform:uppercase;letter-spacing:.4px;color:var(--ink);margin-top:5px}
.contact{position:absolute;left:18px;list-style:none}
.contact li{display:flex;align-items:center;gap:6px;color:var(--red);font-weight:700;font-size:12.5px;margin-bottom:10px}
.contact svg{width:14px;height:14px}
.contact--front{top:120px}
.address{position:absolute;left:248px;top:16px;font-weight:700;font-size:12.5px;color:var(--ink)}
.map{position:absolute;left:280px;top:38px;width:155px;height:118px;border:2px solid var(--red);border-radius:8px;background:linear-gradient(135deg,var(--map-a),var(--map-b))}

/* back */
.equity-heading{height:73px;text-align:center;color:var(--navy-text);font-weight:900;font-size:25.5px;line-height:1.28;padding-top:9px}
.photo--team{height:195px;background:linear-gradient(100deg,#dfe5ea 0%,var(--photo-cool-a) 35%,#e2d6cc 55%,var(--photo-cool-b) 80%,#d8dee6 100%)}
.back-info{background:var(--navy);height:165px;color:var(--white);text-align:center;font-size:9.3px;line-height:1.5;padding:8px 24px 0}
.back-info p{margin-bottom:13px}
.warning{height:46px;text-align:center;font-size:9.3px;line-height:1.5;color:var(--navy-text);padding:6px 20px 0}
.warning__label{background:var(--red);color:var(--white);padding:0 2px;text-transform:uppercase}
.back-footer{background:var(--navy);height:163px;position:relative;color:var(--white)}
.brand--realty{left:16px;top:36px;width:190px}
.brand--realty .brand__name{color:var(--sky);font-size:19px}
.brand--realty .brand__tag{color:var(--white);font-size:7.5px}
.slogan{position:absolute;left:218px;top:14px;width:210px;text-align:center;font-weight:900;font-size:17px;line-height:1.35;text-transform:uppercase}
.back-footer__cta{position:absolute;left:0;right:0;top:120px;text-align:center;font-weight:700;font-size:12px}
.back-footer .call-line{position:absolute;left:0;right:0;top:138px;margin:0}
.back-footer .call-line__text{font-size:12.5px}
</style>
</head>
<body>

<section class="flyer flyer--front">
  <header class="promo-band">
    <h1 class="promo-band__title">'GET YOUR MORTGAGE IN SHAPE FOR SUMMER'</h1>
    <p class="promo-band__sub">Refinance today &amp; potentially receive upwards of $1,500*</p>
  </header>
  <div class="photo photo--couple" role="img" aria-label="Photo of a smiling couple"></div>
  <div class="front-info">
    <h2 class="front-info__heading">HOME LOAN AND INVESTMENT PROPERTY SPECIALIST</h2>
    <p class="front-info__body">Re-finance before 2015 and not only will your Mortgage specialist find you a better product, but they will also rebate you 50% of their brokering commission. An average $500,000 loan is likely to result in over $1,500 cash back. Has there ever been a better reason to refinance?</p>
    <div class="pill-row">
      <div class="pill pill--left">5% of profits donated to<br>our partner Open Harvest</div>
      <div class="pill pill--right">Mobile broker to your<br>door, at your convenience</div>
    </div>
    <p class="front-info__free">100% FREE SERVICE</p>
    <div class="call-line"><span class="call-line__text">CALL NOW 0400 372 948</span></div>
  </div>
  <footer class="front-footer">
    <div class="brand brand--mortgages">
      <div class="brand__row">
        <svg class="brand__mark" viewBox="0 0 16 16" aria-hidden="true"><rect width="16" height="16" fill="var(--red)"/></svg>
        <span class="brand__name">Brisk Home Loans</span>
      </div>
      <span class="brand__tag">Is your mortgage in good shape?</span>
    </div>
    <ul class="contact contact--front">
      <li><svg viewBox="0 0 14 14" aria-hidden="true"><rect x="1" y="3" width="12" height="8" fill="var(--ink)"/><path d="M1 3 L7 8 L13 3" stroke="#fff" stroke-width="1.2" fill="none"/></svg>dale@briskhomeloans.com.au</li>
      <li><svg viewBox="0 0 14 14" aria-hidden="true"><circle cx="7" cy="7" r="6" fill="var(--ink)"/><path d="M1 7 H13 M7 1 C4 4 4 10 7 13 M7 1 C10 4 10 10 7 13" stroke="#fff" stroke-width="0.9" fill="none"/></svg>www.briskhomeloans.com.au</li>
    </ul>
    <p class="address">18 Banksia Road, Elmvale 2771</p>
    <div class="map" role="img" aria-label="Street map showing the office location"></div>
  </footer>
</section>

<section class="flyer flyer--back">
  <h1 class="equity-heading">WHAT ARE YOU DOING<br>WITH YOUR EQUITY?</h1>
  <div class="photo photo--team" role="img" aria-label="Photo of business people in an office with a world map behind"></div>
  <div class="back-info">
    <p>Speak to our investment specialist today &amp; find out how you could potentially use your equity to build a positively geared investment portfolio without spending your own money.</p>
    <p>Keel Realty Advisory will not sell you property, only provide transparent guidance so ultimately you can make an informed decision.</p>
    <p>It is correct nothing is for free, however, unlike most property investment advisers the only payment/commission Keel Realty Advisory receives is that paid from the bank through brokering the loan on your investment property (should you choose to purchase a property and allow us to broker your loan)</p>
  </div>
  <p class="warning"><span class="warning__label">Warning:</span> Beware of typical 'Free' investment seminars where you are ultimately guided down a path to overprized, commission packed, apartments or house and land packages</p>
  <footer class="back-footer">
    <div class="brand brand--realty">
      <div class="brand__row">
        <svg class="brand__mark" viewBox="0 0 16 16" aria-hidden="true"><rect width="16" height="16" fill="var(--sky)"/></svg>
        <span class="brand__name">Keel Realty Advisory</span>
      </div>
      <span class="brand__tag">Cutting out the fatty commissions</span>
    </div>
    <p class="slogan">Your actions<br>today will<br>determine how you<br>live tomorrow</p>
    <p class="back-footer__cta">Call today for further information of this amazing offer</p>
    <div class="call-line"><span class="call-line__text">CALL NOW 0400 372 948</span></div>
  </footer>
</section>

</body>
</html>
```